Linwell Psychology website transfer from WIX to Wordpress

I have a website currently coded in WIX and I want it (or something like it or better) designed to be coded on Wordpress instead. The website should have mobile optimization so that it can be viewed on mobile devices.

The current website is at: www.linwellpsychology.example

I'm not looking for versions of the website that are very different to what I already have, unless they improve on it aesthetically. I'm mainly looking to have a Wordpress version of this website that I built, away from the WIX ecosystem.
Updates

Need extra days to review

Target Market(s)

Psychology services clients

Coding

Coded - Design and coding required

Number of Pages Required

5+ page

Font styles to use
Serif

Requirements
Must have
• The finished product shoud match my website exactly.
Nice to have
• I'm happy to see new ideas that improve on the current website.
Should not have
• It should not be a different version of my website.

```html
<!DOCTYPE html>
<html lang="en">
<head>
<meta charset="utf-8">
<title>Linwell Psychology</title>
<link rel="stylesheet" href="https://fonts.googleapis.com/css2?family=Playfair+Display:wght@400;500&display=swap">
<style>
:root{
  --green:#2f5a4c;
  --white:#ffffff;
  --ink:#2b2b2b;
  --muted:#8a8a8a;
  --faint:#eeeeee;
  --photo-warm:#8a7468;
  --photo-grey:#6f6b6a;
}
*{margin:0;padding:0;box-sizing:border-box}
html,body{width:1200px;height:4416px;overflow:hidden}
body{position:relative;background:var(--white);font-family:"Playfair Display",Georgia,serif;color:var(--ink)}
.section{position:absolute;left:0;width:1200px}
.abs{position:absolute}
.torn{position:absolute;left:0;width:1200px;height:34px;display:block}
.green{background:var(--green);color:var(--white)}

.brand{position:absolute;display:flex;align-items:center;gap:14px;color:var(--white);font-size:30px;letter-spacing:1px;white-space:nowrap}
.brand .dot{width:16px;height:16px;border-radius:50%;background:var(--white)}

.nav-panel{position:absolute;left:425px;top:0;width:775px;height:80px;background:var(--white)}
.nav{position:absolute;top:28px;left:0;width:100%;font-size:23px;color:var(--ink)}
.nav a{position:absolute;color:inherit;text-decoration:none;transform:translateX(-50%)}

.hero-photo{left:103px;top:339px;width:386px;height:703px;border-radius:48% 44% 46% 50% / 30% 26% 30% 34%;background:linear-gradient(160deg,#c9c3bd,#7a5a50 45%,#3a3330)}
.hero-title{left:567px;top:262px;width:560px;text-align:center;font-size:36px;font-weight:400}
.hero-sub{left:567px;top:322px;width:560px;text-align:center;font-size:16px;line-height:23px}
.hero-copy{left:567px;top:428px;width:588px;font-size:13.6px;line-height:21.4px}
.hero-copy p{margin-bottom:21.4px}

.carousel-card{top:1365px;width:292px;height:339px;border:1px solid #555;display:flex;align-items:center;justify-content:center;text-align:center;color:var(--white);font-size:10px;padding:0 14px}
.carousel-card span{position:relative}
.arrow-btn{top:1517px;width:58px;height:57px;background:var(--green);display:flex;align-items:center;justify-content:center}
.dot-nav{top:1774px;width:24px;height:24px;border-radius:50%;border:2px solid var(--green)}
.dot-nav.filled{background:var(--green)}

.about-title{left:142px;top:2195px;width:560px;font-size:34px;line-height:42px;font-weight:400}
.about-copy{left:142px;top:2296px;width:560px;font-size:13.6px;line-height:21.4px}
.about-link{left:142px;top:2424px;font-size:13.6px}
.about-photo{left:783px;top:2057px;width:292px;height:535px;border-radius:50% 46% 48% 50% / 28% 30% 34% 32%;background:linear-gradient(170deg,#b39b8c,#b1624a 55%,#3c4a3f)}

.services-title{left:0;top:2900px;width:1200px;text-align:center;font-size:36px;font-weight:400}
.service{top:3050px;width:330px;height:330px;text-align:center;color:var(--ink)}
.service .bg{position:absolute;left:0;top:0;width:100%;height:100%;border:2px solid var(--faint);border-radius:38% 30% 42% 32%;transform:rotate(-8deg)}
.service h3{position:relative;margin-top:72px;font-size:28px;line-height:34px;font-weight:400}
.service p{position:relative;margin:16px auto 0;width:276px;font-size:13.2px;line-height:21.4px;color:var(--muted)}
.service .btn{position:relative;display:inline-block;margin-top:16px;padding:5px 18px;border-radius:16px;background:var(--green);color:var(--white);font-size:12px}

.hours{left:0;top:3820px;width:1200px;text-align:center;font-size:16px;line-height:38.5px}
.foot-col{top:4030px;font-size:14.2px;line-height:22.3px}
.flags{left:475px;top:4362px;display:flex;gap:8px}
.flag{width:41px;height:27px}
</style>
</head>
<body>
<svg width="0" height="0" style="position:absolute">
  <symbol id="tear" viewBox="0 0 1200 34" preserveAspectRatio="none">
    <path d="M0,34 L0,16 L40,11 L70,18 L110,8 L150,15 L190,9 L230,17 L270,6 L300,13 L350,10 L390,18 L430,9 L470,13 L510,5 L560,15 L600,10 L640,17 L690,7 L730,14 L770,10 L820,18 L860,8 L900,13 L950,6 L990,15 L1030,10 L1080,17 L1120,8 L1160,13 L1200,10 L1200,34 Z"/>
  </symbol>
</svg>

<!-- Hero -->
<section class="section green" style="top:0;height:1200px">
  <div class="brand" style="left:40px;top:28px;font-size:28px"><span class="dot"></span>Linwell Psychology</div>
  <div class="nav-panel">
    <nav class="nav">
      <a style="left:141px">Home</a>
      <a style="left:257px">About</a>
      <a style="left:388px">Services</a>
      <a style="left:520px">FAQs</a>
      <a style="left:634px">Contact</a>
    </nav>
  </div>
  <svg class="torn" style="left:425px;width:775px;top:78px;transform:scaleY(-1);fill:var(--white)"><use href="#tear"/></svg>

  <div class="abs hero-photo" role="img" aria-label="Portrait photo of the psychologist writing notes in an armchair"></div>
  <h1 class="abs hero-title">Dr Elias Marrow</h1>
  <div class="abs hero-sub">Clinical and Counselling Psychologist<br>Clinical Psychosexual Therapist</div>
  <div class="abs hero-copy">
    <p>My name is Elias (he/they) and I am a Clinical and Counselling Psychologist, and accredited Clinical Psychosexual Therapist, with over 15 years' experience working with adults and young people of all abilities and identities.</p>
    <p>My practice focuses on sex therapy and working with diversity, which regularly includes supporting members of LGBTQIA+, neurodivergent, and disabled communities. Because of this work, I am sex-positive and kink-, polyamory-, LGBTQIA+ and neurodiversity knowledgeable and affirming in my practice. I am also a member of many lived experience communities as part of my commitment to lifelong learning and honoring lived experience.</p>
    <p>I know that seeing a therapist can sometimes be anxiety-evoking, and as such, I always aim to curate a non-judgmental, collaborative, and intentional approach to working with people toward their personal goals and a life of value.</p>
    <p>In my work, I balance supportive counselling with evidence-based therapies, such as: humanistic therapy, cognitive-behavioural therapy, acceptance and commitment therapy, compassion-focused therapy, and solution-focused counselling. My work is also underpinned by intersectional feminist and social justice frameworks. As part of ensuring that you are benefiting from your sessions, I will regularly check in to see if you're finding your session helpful to ensure you feel understood, respected, and that your sessions are relevant and on track.</p>
    <p>In addition to my client work, I am also a board accredited CSAB supervisor and enjoy supporting and supervising the practice of other clinicians, both trainee and experienced. And enjoy consultancy and training work with practices and organisations.</p>
  </div>
</section>

<!-- Focus carousel -->
<section class="section" style="top:1200px;height:720px">
  <svg class="torn" style="top:-16px;fill:var(--white)"><use href="#tear"/></svg>
</section>
<div class="abs arrow-btn" style="left:21px"><svg width="24" height="40" viewBox="0 0 24 40"><path d="M20 4 L4 20 L20 36" fill="none" stroke="#fff" stroke-width="2"/></svg></div>
<div class="abs carousel-card" style="left:125px;background:linear-gradient(135deg,#77706c,#5f5a58)" role="img" aria-label="Photo of two smiling women"><span>Sexual Identity &amp; Diversity</span></div>
<div class="abs carousel-card" style="left:454px;background:linear-gradient(135deg,#7a716c,#625b58)" role="img" aria-label="Photo of a couple embracing"><span>Sex Education &amp; Empowerment</span></div>
<div class="abs carousel-card" style="left:783px;background:linear-gradient(135deg,#7d7671,#67615e)" role="img" aria-label="Photo of two men laughing together"><span>Mismatched Libido &amp; Sex 'Addiction'</span></div>
<div class="abs arrow-btn" style="left:1104px"><svg width="24" height="40" viewBox="0 0 24 40"><path d="M4 4 L20 20 L4 36" fill="none" stroke="#fff" stroke-width="2"/></svg></div>
<div class="abs dot-nav filled" style="left:545px"></div>
<div class="abs dot-nav" style="left:588px"></div>
<div class="abs dot-nav filled" style="left:629px"></div>

<!-- About therapy -->
<section class="section green" style="top:1920px;height:857px">
  <svg class="torn" style="top:-30px;fill:var(--green)"><use href="#tear"/></svg>
</section>
<h2 class="abs about-title" style="color:var(--white)">What is a Clinical Psychosexual Therapist</h2>
<p class="abs about-copy" style="color:var(--white)">Sometimes referred to as a sex therapist, a Clinical Psychosexual Therapist is someone who has postgraduate university qualifications in the field of human sexuality, which is a broad area encompassing subjects like: sexual orientation, gender identity, sexual function and diversity, sexual and reproductive health, intersectional feminism, relationship dynamics, and sexual trauma.</p>
<a class="abs about-link" style="color:var(--white)">| How can a clinical psychosexual therapist help me? |</a>
<div class="abs about-photo" role="img" aria-label="Photo of a laughing couple hugging"></div>

<!-- Services -->
<section class="section" style="top:2777px;height:797px">
  <svg class="torn" style="top:-30px;fill:var(--white)"><use href="#tear"/></svg>
</section>
<h2 class="abs services-title">What Services I offer</h2>
<div class="abs service" style="left:61px">
  <div class="bg" role="img" aria-label="Faint geometric line decoration"></div>
  <h3>Psychological<br>Therapy</h3>
  <p>Psychological assessment, education, counselling, and therapy using person-centered and evidence-based integrative therapeutic interventions</p>
  <span class="btn">Learn More</span>
</div>
<div class="abs service" style="left:461px">
  <div class="bg" role="img" aria-label="Faint geometric line decoration"></div>
  <h3>Clinical<br>Supervision</h3>
  <p>Clinical supervision to support provisional psychologists and registrars, early career mentoring, technical skill building, and clinical case discussion.</p>
  <span class="btn">Learn More</span>
</div>
<div class="abs service" style="left:824px">
  <div class="bg" role="img" aria-label="Faint geometric line decoration"></div>
  <h3>Training and<br>Consultancy</h3>
  <p>Training for general psychology or special interest subjects like sexology and neurodivergence, and consultancy for practices and organisations.</p>
  <span class="btn">Learn More</span>
</div>

<!-- Footer -->
<footer class="section green" style="top:3574px;height:842px">
  <svg class="torn" style="top:-30px;fill:var(--green)"><use href="#tear"/></svg>
  <div class="brand" style="left:0;width:1200px;justify-content:center;top:148px;font-size:34px"><span class="dot"></span>Linwell Psychology</div>
</footer>
<div class="abs hours" style="color:var(--white)">Practice Hours<br>(by appointment only):<br>Mondays 9:30am - 3:30pm<br>Thursdays: 8:30am - 2:30pm</div>
<p class="abs foot-col" style="left:21px;width:270px;color:var(--white)">At Linwell Psychology, we welcome people of all backgrounds, race, ethnicity, genders, sexuality, relationship type, neurotype, and abilities. Please contact us if we can assist you to make your appointment more inclusive in any way or provide us feedback on how we can do better.</p>
<p class="abs foot-col" style="left:400px;width:372px;text-align:center;color:var(--white)">If you need support between appointments or after hours, please consider contacting:<br><br>Harbourline on 13 20 40<br>Youth Talkline on 1800 000 201<br>MenSpeak on 1300 000 302<br>Crisis Return Line on 1300 000 403<br>Clearsky Support on 1300 000 504<br>Mindroom on 1800 000 605<br>RainbowTalk on 1800 000 706<br>13KIN on 13 00 07</p>
<p class="abs foot-col" style="left:855px;width:328px;color:var(--white)">We acknowledge the Traditional Custodians of the lands upon which we work here in Meanjin, the Turrbal and Jagera people, as the first inhabitants of our nation. We recognise their continuing connection to land, water, and culture and pay our respects to their Elders past, present, and emerging - as well as First Nations people and the stolen generation who have yet to find their home. Their lands never ceded sovereignty. Always was, always will be, Aboriginal land.</p>
<div class="abs flags">
  <div class="flag" style="background:linear-gradient(#c0504d,#d9a441,#6a9a5b,#4d6fa8)"></div>
  <div class="flag" style="background:#d9a441"></div>
  <div class="flag" style="background:linear-gradient(#7fb7d8,#e8a9b8,#f4f4f4)"></div>
  <div class="flag" style="background:linear-gradient(#1b1b1b 50%,#b03a2e 50%)"></div>
  <div class="flag" style="background:linear-gradient(#3f8a5a 25%,#2c4a94 25%,#2c4a94 75%,#3f8a5a 75%)"></div>
</div>
</body>
</html>
```